Design Contest For Business Cards and PostCards (over-sized/standard)

Type of Contest : Business Card and PostCard Design

Size Requirements : Not 100% sure, whatever size looks best for both business cards and the postcards.

Color Requirements : Include colors from the Logo provided

General Requirements : I will need the template and the formats of both the business card and the postcard at the time of completion and upon receiving payment. Must include logo provided.

Additional Information : I'm a personal trainer that provides fitness instruction and helps clients achieve their goals through exercise and nutrition. Information is below
Business Card:
Company: LUMEN CORE WELLNESS
Personal Training|Bootcamp|Kickboxing|Nutrition
Name: Dorian Kessler
Website: LumenCoreWellness.example
Phone: 555.203.7719
Addtl: Somewhere it should say, "Schedule your free session or assessment today" and a quote that says, “Motivation is what gets you started. Habit is what keeps you going.” or "Lumen your Fitness"

PostCard (for mailing to potential customers' households)
Company: LUMEN CORE WELLNESS
Name: Dorian Kessler
Phone: 555.203.7719
**Try a free week of Lumen Core Bootcamp**

***The rest of the creativity is up to the designer and i'm looking for double sided on both. I will be using the winning design to upload to either a quillora or something like it. Thank you.

```html
<!DOCTYPE html>
<html lang="en">
<head>
<meta charset="utf-8">
<title>Lumen Core Wellness – Business Card &amp; Postcard</title>
<link rel="stylesheet" href="https://fonts.googleapis.com/css2?family=Open+Sans:wght@400;600;700&family=Roboto+Condensed:wght@700&display=swap">
<style>
  :root {
    --sky: #76aecb;
    --lime: #b2d56f;
    --royal: #125c91;
    --navy: #243a4e;
    --cream: #f3efe6;
    --mist: #edf3fa;
    --ink: #1f2a36;
    --paper: #ffffff;
    --stage: #ebebeb;
    --rule: #9fb9cf;
  }
  * { box-sizing: border-box; margin: 0; padding: 0; }
  html, body { width: 1200px; height: 1134px; overflow: hidden; }
  body { background: var(--stage); font-family: "Open Sans", sans-serif; position: relative; }

  .card { position: absolute; overflow: hidden; }

  /* Business card */
  .business-card { left: 68px; top: 36px; width: 784px; height: 507px; background: var(--cream); }
  .business-card .top-band { position: absolute; left: 0; top: 0; width: 100%; height: 91px; background: var(--sky); }
  .business-card .accent-band { position: absolute; left: 0; top: 91px; width: 100%; height: 48px; background: var(--lime); }
  .offer-box { position: absolute; left: 65px; top: 0; width: 234px; height: 165px; background: var(--royal); color: var(--paper);
    font-size: 20px; line-height: 1; display: flex; flex-direction: column; justify-content: center; align-items: center;
    gap: 26px; padding: 6px 8px 0; text-align: center; white-space: nowrap; }
  .trainer { position: absolute; right: 35px; top: 20px; text-align: right; color: var(--ink); }
  .trainer-name { font-weight: 700; font-size: 33px; line-height: 1.05; }
  .trainer-role { font-size: 21px; line-height: 1.2; }
  .phone { position: absolute; right: 35px; top: 99px; height: 32px; display: flex; align-items: center; gap: 8px;
    font-weight: 700; font-size: 23px; color: var(--navy); }
  .phone svg { width: 20px; height: 22px; }
  .photo { position: absolute; left: 375px; top: 139px; width: 409px; height: 312px;
    background: linear-gradient(90deg, #efe9df 0%, #c9a18a 30%, #b4846a 50%, #d8c1b2 70%, #f2ece4 100%); }
  .brand { position: absolute; display: flex; align-items: center; gap: 14px; color: var(--ink); font-weight: 700; }
  .brand-dot { border-radius: 50%; background: var(--royal); flex: none; }
  .brand-name { line-height: 1.08; letter-spacing: 1px; white-space: nowrap; }
  .business-card .brand { left: 34px; top: 250px; }
  .business-card .brand-dot { width: 36px; height: 36px; }
  .business-card .brand-name { font-size: 36px; }
  .quote { position: absolute; left: 26px; right: 20px; top: 402px; text-align: center; font-family: "Roboto Condensed", sans-serif;
    font-weight: 700; font-size: 27px; letter-spacing: -0.6px; color: var(--lime); text-shadow: 1px 1px 1px #3d4a2a; white-space: nowrap; }
  .footer { position: absolute; left: 0; bottom: 0; width: 100%; height: 56px; background: var(--navy); color: var(--paper);
    font-weight: 700; font-size: 23px; display: flex; align-items: center; justify-content: center; white-space: nowrap; }

  /* Postcard */
  .postcard { left: 339px; top: 590px; width: 787px; height: 508px; background: var(--paper); }
  .message-panel { position: absolute; left: 0; top: 0; width: 373px; height: 100%; background: var(--mist); }
  .message-panel .top-band { position: absolute; left: 0; top: 0; width: 100%; height: 91px; background: var(--sky);
    display: flex; align-items: center; justify-content: center; padding-top: 12px;
    font-family: "Roboto Condensed", sans-serif; font-weight: 700; font-size: 31px; color: var(--ink); }
  .message-panel .accent-band { position: absolute; left: 0; top: 91px; width: 100%; height: 51px; background: var(--lime); }
  .message-panel .brand { left: 52px; top: 200px; }
  .message-panel .brand-dot { width: 30px; height: 30px; }
  .message-panel .brand-name { font-size: 30px; }
  .message-panel .footer { font-size: 18px; padding: 0 10px; }
  .cta { position: absolute; left: 0; width: 100%; top: 372px; text-align: center; font-size: 22px; line-height: 1.4; color: var(--ink); }
  .stamp-box { position: absolute; left: 623px; top: 25px; width: 137px; height: 106px; border: 1.5px solid var(--rule); }
  .address-line { position: absolute; left: 453px; width: 307px; height: 0; border-top: 1.5px solid var(--rule); }
</style>
</head>
<body>

<section class="card business-card">
  <div class="top-band"></div>
  <div class="accent-band"></div>
  <div class="offer-box"><span>Try a free week of</span><span>Lumen Core Bootcamp</span></div>
  <div class="trainer">
    <div class="trainer-name">Dorian Kessler</div>
    <div class="trainer-role">personal trainer</div>
  </div>
  <div class="phone">
    <svg viewBox="0 0 20 22" aria-hidden="true"><path fill="currentColor" d="M5 1l3 5-2.2 2c1 3 3 5.5 5.8 7.2l2-2.2 5 3-1.6 3.6C12 21 3 12 1.5 4.2z"/></svg>
    <span>555.203.7719</span>
  </div>
  <div class="photo" role="img" aria-label="Photo of a fit man and woman in workout clothing, shown from the torso"></div>
  <div class="brand"><span class="brand-dot"></span><span class="brand-name">LUMEN CORE<br>WELLNESS</span></div>
  <p class="quote">Motivation is what gets you started. Habit is what keeps you going</p>
  <div class="footer">www.LumenCoreWellness.example</div>
</section>

<section class="card postcard">
  <div class="message-panel">
    <div class="top-band">Lumen Your Fitness</div>
    <div class="accent-band"></div>
    <div class="brand"><span class="brand-dot"></span><span class="brand-name">LUMEN CORE<br>WELLNESS</span></div>
    <p class="cta">Schedule your free session<br>or assessment today</p>
    <div class="footer">www.LumenCoreWellness.example</div>
  </div>
  <div class="stamp-box"></div>
  <div class="address-line" style="top:219px"></div>
  <div class="address-line" style="top:292px"></div>
  <div class="address-line" style="top:363px"></div>
</section>

</body>
</html>
```